Innovative Veterinary Clinic Business Card

We are a mixed animal veterinary practice in rural Queensland. Our patients include cattle, horses, dogs and cats, with everything in between. We are moving the clinic forward to become the best in our region and one of the best in the State, with gold standard service and standards of care, while remaining down to earth and genuine. Our current motto is - "The difference is, we care". The clinic colours are blue and red but am open to change. I would like something innovative and modern, that stands out and says we are different, we are amazing, and our patients come first. Something that will be remembered. Our current logo and business card I feel are empty and don't stand out.
Updates

please use font that is strong but simple. I am looking for something different, rather than your run of the mill business card. I am open to anything - as long as it has two sides and defines us, I'll consider all submissions. Thank you for your efforts, they are all very much appreciated!!

Thank you all very much for your amazing efforts. I wasn't expecting to have such a great response, so I thank you for your participation. You are all very talented and I loved your designs. I wish you all the best for the future. Thank you!

Target Market(s)

pet owners, graziers, horse clients (horses of all types - pets, campdrafting, mustering, polocrosse, thoroughbreds, show ponies)

Industry/Entity Type

Veterinary

Contact Information for Business Card

Dr. Freya L Tovell - BVSc (Hons)
Creekbend Veterinary Services
17 Harrow St
Wattlegrove, QLD, 4699
Ph: 0741872306 or 0418365947
Fax: 0741872309
e: creekbendvets@mailnest.example

Colors

Designer to choose colors to be used in the design.

Requirements
Must have
• back side of card to be used as an appointment card
Nice to have
• perhaps a photo of an animal (horse, dog, cat, cattle)
Should not have
• I don't want the standard name, rank and serial number business card. No cartoon animals.

```html
<!DOCTYPE html>
<html lang="en">
<head>
<meta charset="utf-8">
<title>Creekbend Veterinary Services – Business Card</title>
<link rel="stylesheet" href="https://fonts.googleapis.com/css2?family=Open+Sans:wght@400;600;700;800&display=swap">
<style>
  :root {
    --page-bg: #e9e7e4;
    --card-white: #ffffff;
    --blue-deep: #1f3f86;
    --blue-mid: #2b62ad;
    --blue-bright: #3a86c8;
    --red-accent: #d2253a;
    --text-white: #ffffff;
    --line-teal: #5aa7a5;
    --label-blue: #3a6fb3;
  }
  * { box-sizing: border-box; margin: 0; padding: 0; }
  html, body {
    width: 1200px; height: 800px; overflow: hidden;
    background: var(--page-bg);
    font-family: "Open Sans", Arial, sans-serif;
  }
  .canvas {
    position: relative; width: 1200px; height: 800px;
    display: flex; align-items: center; justify-content: center; gap: 40px;
  }
  .card {
    position: relative; width: 540px; height: 330px;
    border-radius: 14px; overflow: hidden;
    box-shadow: 0 6px 18px rgba(0,0,0,0.18);
  }

  /* Back: appointment card */
  .card-back { background: var(--card-white); }
  .appointment {
    position: absolute; left: 30px; top: 26px; width: 300px;
    color: var(--label-blue); font-size: 15px; font-weight: 600;
  }
  .appointment-row {
    display: flex; align-items: flex-end; gap: 8px; height: 34px;
  }
  .appointment-row .field-line {
    flex: 1; border-bottom: 1.5px dotted var(--line-teal); margin-bottom: 4px;
  }
  .back-brand {
    position: absolute; left: 30px; top: 170px;
    color: var(--blue-mid); font-weight: 800; line-height: 1.05;
  }
  .back-brand .brand-main { font-size: 44px; letter-spacing: 1px; }
  .back-brand .brand-sub { font-size: 19px; letter-spacing: 0.5px; }
  .back-art { position: absolute; right: 0; top: 0; width: 220px; height: 330px; }

  /* Front: details */
  .card-front { background: linear-gradient(160deg, var(--blue-bright), var(--blue-deep)); }
  .front-art { position: absolute; inset: 0; width: 540px; height: 330px; }
  .front-brand {
    position: absolute; left: 236px; top: 34px;
    display: flex; align-items: center; gap: 10px;
    color: var(--blue-deep); font-weight: 800; line-height: 1.05;
  }
  .front-brand .brand-dot {
    width: 24px; height: 24px; border-radius: 50%; background: var(--blue-deep);
  }
  .front-brand .brand-main { font-size: 30px; letter-spacing: 1px; }
  .front-brand .brand-sub { font-size: 14px; }
  .vet-name {
    position: absolute; left: 26px; top: 150px;
    color: var(--text-white); font-size: 16px; font-weight: 700;
  }
  .contact-list {
    position: absolute; left: 26px; top: 184px; list-style: none;
    color: var(--text-white); font-size: 12.5px; line-height: 1.55;
  }
  .contact-list li { display: flex; align-items: center; gap: 7px; }
  .contact-icon { width: 12px; height: 12px; flex: none; }
  .clinic-address {
    position: absolute; right: 28px; bottom: 18px;
    color: var(--text-white); font-size: 13px; line-height: 1.4; font-style: normal;
  }
  .clinic-address .clinic-name { font-weight: 700; }
</style>
</head>
<body>
<main class="canvas">

  <section class="card card-back" aria-label="Appointment card, back side">
    <div class="appointment">
      <div class="appointment-row"><span>Next Appointment:</span><span class="field-line"></span></div>
      <div class="appointment-row"><span>Date:</span><span class="field-line"></span></div>
      <div class="appointment-row"><span>Time:</span><span class="field-line"></span></div>
    </div>
    <div class="back-brand">
      <div class="brand-main">CREEKBEND</div>
      <div class="brand-sub">Veterinary Services</div>
    </div>
    <svg class="back-art" viewBox="0 0 220 330" role="img" aria-label="Blue silhouettes of a horse, dog and cat">
      <defs>
        <linearGradient id="silhouette-tone" x1="0" y1="0" x2="1" y2="1">
          <stop offset="0" stop-color="#3a86c8"/>
          <stop offset="1" stop-color="#1f4f9a"/>
        </linearGradient>
      </defs>
      <path d="M220,0 L110,0 Q40,80 60,170 Q30,250 70,330 L220,330 Z" fill="url(#silhouette-tone)"/>
    </svg>
  </section>

  <section class="card card-front" aria-label="Business card, front side">
    <svg class="front-art" viewBox="0 0 540 330" aria-hidden="true">
      <defs>
        <linearGradient id="photo-tone" x1="0" y1="0" x2="1" y2="1">
          <stop offset="0" stop-color="#dbe8f3"/>
          <stop offset="0.45" stop-color="#a9cf79"/>
          <stop offset="0.7" stop-color="#7fb04d"/>
          <stop offset="1" stop-color="#7a3a22"/>
        </linearGradient>
      </defs>
      <path d="M170,0 Q270,200 540,235 L540,0 Z" fill="url(#photo-tone)" role="img" aria-label="Photo of a red-brown cow in a green paddock"/>
      <path d="M170,0 Q270,200 540,235" fill="none" stroke="#d2253a" stroke-width="9"/>
      <path d="M158,0 Q256,210 540,248" fill="none" stroke="#ffffff" stroke-opacity="0.35" stroke-width="2"/>
    </svg>
    <div class="front-brand">
      <span class="brand-dot"></span>
      <div>
        <div class="brand-main">CREEKBEND</div>
        <div class="brand-sub">Veterinary Services</div>
      </div>
    </div>
    <div class="vet-name">Dr. Freya L Tovell - BVSc (Hons)</div>
    <ul class="contact-list">
      <li>
        <svg class="contact-icon" viewBox="0 0 12 12" aria-hidden="true"><rect width="12" height="12" rx="2" fill="#fff"/><path d="M3.5 2.5h1.5l.7 2-1 .7a5 5 0 0 0 2.1 2.1l.7-1 2 .7v1.5a1 1 0 0 1-1 1A6 6 0 0 1 2.5 3.5a1 1 0 0 1 1-1z" fill="#2b62ad"/></svg>
        <span>0741872306</span>
      </li>
      <li>
        <svg class="contact-icon" viewBox="0 0 12 12" aria-hidden="true"><rect width="12" height="12" rx="2" fill="#fff"/><rect x="4" y="2" width="4" height="8" rx="1" fill="#2b62ad"/></svg>
        <span>0418365947</span>
      </li>
      <li>
        <svg class="contact-icon" viewBox="0 0 12 12" aria-hidden="true"><rect width="12" height="12" rx="2" fill="#fff"/><rect x="2.5" y="5" width="7" height="4.5" fill="#2b62ad"/><rect x="4" y="2.5" width="4" height="2.5" fill="#2b62ad"/></svg>
        <span>0741872309</span>
      </li>
      <li>
        <svg class="contact-icon" viewBox="0 0 12 12" aria-hidden="true"><rect width="12" height="12" rx="2" fill="#fff"/><path d="M2.5 3.5h7v5h-7z M2.5 3.5l3.5 3 3.5-3" fill="none" stroke="#2b62ad" stroke-width="1"/></svg>
        <span>creekbendvets@mailnest.example</span>
      </li>
    </ul>
    <address class="clinic-address">
      <div class="clinic-name">Creekbend Veterinary Services</div>
      <div>17 Harrow St Wattlegrove</div>
      <div>QLD, 4699</div>
    </address>
  </section>

</main>
</body>
</html>
```